The Perfect Business Card for PineHarbor

I am looking for a business card which beautifully incorporates my logo, reflects my business and looks special, elegant and clean.

```html
<!DOCTYPE html>
<html lang="en">
<head>
<meta charset="utf-8">
<title>PineHarbor Business Card</title>
<link rel="stylesheet" href="https://fonts.googleapis.com/css2?family=Lora:wght@400;600&display=swap">
<style>
  :root {
    --backdrop: #e4e5e3;
    --card: #ffffff;
    --green: #5a8333;
    --green-dark: #4a6f2a;
    --green-light: #7ba343;
    --ink-light: #ffffff;
    --shadow: rgba(0, 0, 0, 0.18);
  }
  * { box-sizing: border-box; margin: 0; padding: 0; }
  html, body { width: 1200px; height: 900px; overflow: hidden; }
  body {
    background: var(--backdrop);
    font-family: "Lora", Georgia, serif;
    position: relative;
  }
  .card {
    position: absolute;
    width: 600px;
    height: 343px;
    background: var(--card);
    box-shadow: 0 10px 30px var(--shadow);
    overflow: hidden;
  }
  .card--front { left: 110px; top: 80px; }
  .card--back  { left: 490px; top: 475px; }

  .brand {
    position: absolute;
    display: flex;
    align-items: center;
    gap: 14px;
  }
  .brand__mark {
    border: 2px solid var(--green);
    border-radius: 50%;
    flex: none;
  }
  .brand__name {
    color: var(--green);
    font-weight: 400;
    letter-spacing: 0.04em;
    line-height: 1;
    white-space: nowrap;
  }
  .card--front .brand { left: 150px; top: 130px; }
  .card--front .brand__mark { width: 78px; height: 78px; }
  .card--front .brand__name { font-size: 46px; }

  .card--back .brand { left: 26px; top: 248px; }
  .card--back .brand__mark { width: 66px; height: 66px; }
  .card--back .brand__name { font-size: 40px; }

  .discs { position: absolute; inset: 0; }

  .person {
    position: absolute;
    left: 186px; top: 124px;
    width: 140px;
    text-align: center;
    color: var(--ink-light);
  }
  .person__name { font-size: 14px; font-weight: 600; letter-spacing: 0.05em; text-transform: uppercase; white-space: nowrap; }
  .person__role { font-size: 13px; margin-top: 2px; }

  .contact {
    position: absolute;
    left: 352px; top: 90px;
    list-style: none;
    color: var(--ink-light);
    font-size: 13px;
  }
  .contact__item {
    display: flex;
    align-items: center;
    gap: 8px;
    height: 30px;
    white-space: nowrap;
  }
  .contact__icon { width: 13px; height: 13px; flex: none; }
</style>
</head>
<body>

<section class="card card--front" aria-label="Card front">
  <div class="brand">
    <span class="brand__mark"></span>
    <span class="brand__name">PineHarbor</span>
  </div>
</section>

<section class="card card--back" aria-label="Card back">
  <svg class="discs" width="600" height="343" viewBox="0 0 600 343" aria-hidden="true">
    <defs>
      <linearGradient id="disc-fill" x1="0" y1="0" x2="0" y2="1">
        <stop offset="0" stop-color="#4a6f2a"/>
        <stop offset="0.5" stop-color="#7ba343"/>
        <stop offset="1" stop-color="#4a6f2a"/>
      </linearGradient>
    </defs>
    <circle cx="256" cy="142" r="82" fill="url(#disc-fill)"/>
    <circle cx="256" cy="142" r="74" fill="none" stroke="#ffffff" stroke-opacity="0.7" stroke-width="1.5"/>
    <circle cx="452" cy="150" r="136" fill="url(#disc-fill)"/>
    <circle cx="452" cy="150" r="127" fill="none" stroke="#ffffff" stroke-opacity="0.7" stroke-width="1.5"/>
  </svg>

  <div class="person">
    <p class="person__name">Elena Marsh</p>
    <p class="person__role">Director</p>
  </div>

  <ul class="contact">
    <li class="contact__item">
      <svg class="contact__icon" viewBox="0 0 16 16"><path fill="#fff" d="M3 2h3l1 4-2 1c1 2 2 3 4 4l1-2 4 1v3c0 1-1 1-2 1C7 14 2 9 2 4c0-1 0-2 1-2z"/></svg>
      (00) 0000 0000
    </li>
    <li class="contact__item">
      <svg class="contact__icon" viewBox="0 0 16 16"><rect x="1" y="3" width="14" height="10" rx="1" fill="#fff"/><path d="M1.5 4 8 9l6.5-5" fill="none" stroke="#5a8333" stroke-width="1.3"/></svg>
      elena@pineharbor.com
    </li>
    <li class="contact__item">
      <svg class="contact__icon" viewBox="0 0 16 16"><circle cx="8" cy="8" r="6.5" fill="none" stroke="#fff" stroke-width="1.5"/><path d="M1.5 8h13M8 1.5c-3 3-3 10 0 13M8 1.5c3 3 3 10 0 13" fill="none" stroke="#fff" stroke-width="1.2"/></svg>
      www.pineharbor.com
    </li>
    <li class="contact__item">
      <svg class="contact__icon" viewBox="0 0 16 16"><path fill="#fff" d="M8 1a5 5 0 0 1 5 5c0 4-5 9-5 9S3 10 3 6a5 5 0 0 1 5-5z"/><circle cx="8" cy="6" r="2" fill="#5a8333"/></svg>
      00 dummy city, dummy place
    </li>
  </ul>

  <div class="brand">
    <span class="brand__mark"></span>
    <span class="brand__name">PineHarbor</span>
  </div>
</section>

</body>
</html>
```